website design + images

We need a very appealing website design, layout and images for a sales analytics and sales productivity services company based in San Ramon, California. We need a good design for the home page and a template for all other pages (total 2 designs), and images for all inner pages (center column/banner images, and right hand top corner small images). There are about 18 inner pages.
Updates

Our existing website is www.vorlaxen.com
Our corporate colours are the ones that are there on the website. The logo is also shown. We will be changing the tagline to "accelerating revenue" or equivalent of that.

Please use the document "website for vorlaxen - template v2.doc" that I just uploaded for any reference to the content, navigation and wireframes. A few more clarifications are provided mainly for the link "Solutions".

Devendra Kothuri

Hi,
We just uploaded ver 4 of the website template. There is more elaboration provided around the sublinks / sections for Solutions. Pls review and do get back if you need any clarifications.

Rgds
Devendra Kothuri

Hi all,
We have so far received a few good designs. The designs are more or less on the right track. I would like to urge all of you to use the content and navigation provided in the document attached to our brief "website for vorlaxen - template v4.doc".  Please DO NOT use the content in our existing website www.vorlaxen.com . That is very old. We mentioned it only for reference to colour theme and broad details.

We have totally 13 sections in Solutions pages. They may be designed as a tree of links - first level sublinks - second level sublinks or links - first level sublinks and the remaining as sections within the first level sublinks pages. The page design would remain the same for all inner pages except careers. But after finalizing the design for the inner page, we will need images for the different inner pages.

Rgds
Devendra Kothuri

Hi,
Thank you all for participation and very good designs. We are quite happy with what we have seen. We have now shortlisted about 4 vendors and sending invididual feedback to them for further improvement. We will be finalizing by Monday or Tuesday.  To the vendors who do not get feedback from us, thank you very much for participation. We may still do business in future for some of our other needs. 
The following are the process steps / expectations going forward, 
1. Feedback to the shortlisted designers and inviting improvements.
2. Review of the improved designs and further shortlist & feedback or direct finalization.
3. The design should be in 1024*768
2. Number of page designs = 2 (home page, inner page).
4. Home page design: instead of delivery model and customers, show one link "Why Us".
4. Solutions page design:  We will be needing an image in center column of solutions page that in a nutshell gives all the different types of solutions we provide. The entire set of solutions is in our attached document website for vorlaxen - template v4 and I am just uploading v5 with more description on sublinks.
5. After selection, we will be needing images for all the solution pages (total 12 pages under solutions + one solutions page), 1 image for Why Us?, 1 for Careers, and 3 for company (about us/ team, core values, ...) = total 18

Rgds
Devendra Kothuri

Target Market(s)

We are a sales analytics and sales productivity services company. We help B2B companies with: sales planning; sales operations and sales measurement. The characteristics of our customers are:
- B2B medium enterprises (USD 100M- USD 2B in revenue) in the US
- Primary target verticals are: high-tech, engineering and professional services firms
- Our primary target customers titles are VP of Sales or VP of marketing; we could be selling to the CEO at companies with revenues below $200M

Industry/Entity Type

Consulting

Requirements
Must have
• - Clean, uncluttered design
• - Easy navigation; minimum clicks
Nice to have
• We have already built a content management system and wireframes for this site. To the extent possible, it would be great to leverage the wireframe structure we built, provided you don’t have to compromise on the look and feel and navigation of the site. Below is what we currently have as banner sizes and resolutions are:
• Home page banner size: 950 * 250’
• All pages – center top - image size: 558 * 160
• All pages – right hand top image – 175*135’

```html
<!DOCTYPE html>
<html lang="en">
<head>
<meta charset="utf-8">
<title>Vorlaxen – Managed Services</title>
<link rel="stylesheet" href="https://fonts.googleapis.com/css2?family=Source+Sans+3:wght@400;600;700&family=Arimo:wght@400;700&display=swap">
<style>
  :root {
    --blue: #0c6db5;
    --blue-dark: #0a5c9c;
    --green: #4f9a45;
    --green-dark: #3f8438;
    --text: #222;
    --grey-text: #666;
    --white: #fff;
    --grey-bottom: #9b9b9b;
  }
  * { box-sizing: border-box; margin: 0; padding: 0; }
  html, body { width: 1200px; height: 773px; overflow: hidden; }
  body {
    position: relative;
    font-family: "Arimo", Arial, sans-serif;
    color: var(--text);
    background: linear-gradient(#fff 0, #fff 120px, #e6e6e6 330px, #b9b9b9 560px, var(--grey-bottom) 773px);
  }
  .utility-bar {
    position: absolute; left: 0; top: 0; width: 1200px; height: 42px;
    background: linear-gradient(var(--blue), var(--blue-dark));
  }
  .utility-link {
    position: absolute; top: 11px; display: flex; align-items: center; gap: 7px;
    color: var(--white); font-family: "Source Sans 3", sans-serif; font-size: 14px; font-weight: 600;
    text-decoration: none; letter-spacing: 0.2px;
  }
  .utility-link svg { width: 20px; height: 20px; }
  .utility-link.is-account {
    left: 54px; top: 0; width: 160px; height: 51px; padding: 0 0 9px 8px; align-items: flex-start;
    padding-top: 11px;
    background: linear-gradient(#6db55a, var(--green-dark)); border-radius: 0 0 5px 5px;
    box-shadow: 0 2px 3px rgba(0,0,0,.25);
  }
  .brand { position: absolute; left: 62px; top: 88px; }
  .brand-name {
    font-family: "Source Sans 3", sans-serif; font-size: 34px; font-weight: 600;
    color: var(--blue); line-height: 1;
  }
  .brand-tagline {
    margin-top: 8px;
    font-family: "Arimo", Arial, sans-serif; font-size: 14px; color: var(--grey-text);
  }
  .main-nav {
    position: absolute; right: 80px; top: 141px; display: flex; align-items: center;
    font-size: 14px; color: var(--blue);
  }
  .main-nav a { color: var(--blue); text-decoration: none; padding: 0 7px; }
  .main-nav .sep { color: var(--blue); }
  .main-nav a.is-active {
    background: var(--green); color: var(--white); border-radius: 12px; padding: 3px 11px;
    box-shadow: inset 0 0 0 2px #3d7d35; margin-right: 5px;
  }
  .page-panel {
    position: absolute; left: 48px; top: 178px; width: 1090px; height: 550px;
    background: var(--white); border-radius: 0 0 10px 10px;
    box-shadow: 0 4px 10px rgba(0,0,0,.18);
  }
  .side-menu { position: absolute; left: 57px; top: 185px; width: 214px; height: 520px; border-right: 1px solid #ececec; }
  .side-menu-title {
    height: 39px; display: flex; align-items: center; gap: 9px; padding-left: 13px;
    background: linear-gradient(#fff, #dcdcdc); border-radius: 4px 4px 0 0;
    border-bottom: 1px solid #c9c9c9;
    font-family: "Source Sans 3", sans-serif; font-weight: 700; font-size: 16px; color: var(--green);
  }
  .side-menu-title .marker { width: 16px; height: 16px; background: var(--green); border-radius: 2px; display: grid; place-items: center; }
  .side-menu ul { list-style: none; margin: 12px 0 0 14px; width: 194px; }
  .side-menu li {
    height: 25px; line-height: 23px; border-bottom: 1px dotted #9a9a9a;
    font-family: Verdana, "Arimo", sans-serif; font-size: 12.5px; color: #111; padding-left: 11px; position: relative;
  }
  .side-menu li::before {
    content: ""; position: absolute; left: 1px; top: 9px;
    border-left: 4px solid #333; border-top: 3px solid transparent; border-bottom: 3px solid transparent;
  }
  .hero-banner {
    position: absolute; left: 284px; top: 185px; width: 626px; height: 181px;
    background: linear-gradient(100deg, #0f6fb3 0%, #1b9ad8 45%, #4cc2ee 70%, #1b86c6 100%);
  }
  .hero-banner-copy { position: absolute; left: 14px; bottom: 16px; color: var(--white); font-family: "Source Sans 3", sans-serif; }
  .hero-banner-copy h2 { font-size: 26px; font-weight: 700; line-height: 1.1; }
  .hero-banner-copy p { font-size: 17px; font-weight: 600; line-height: 1.15; }
  .feature-card { position: absolute; left: 926px; top: 185px; width: 197px; height: 181px; }
  .feature-card-image { width: 197px; height: 152px; background: linear-gradient(135deg, #7c8a96, #d8dde2 55%, #f2f2f2); }
  .feature-card-caption {
    height: 29px; line-height: 29px; padding-left: 8px; background: var(--green);
    color: var(--white); font-family: "Source Sans 3", sans-serif; font-weight: 700; font-size: 14px;
  }
  .content { position: absolute; left: 287px; top: 378px; width: 621px; }
  .content h1 { font-family: "Source Sans 3", sans-serif; font-weight: 700; line-height: 1.05; }
  .content .kicker { display: block; font-size: 22px; color: var(--blue); }
  .content .title { display: block; font-size: 27px; color: var(--green); }
  .content p { margin-top: 8px; font-size: 13.3px; line-height: 18.6px; text-align: justify; hyphens: auto; }
  .content p + p { margin-top: 18px; }
  .aside-copy {
    position: absolute; left: 926px; top: 380px; width: 197px; height: 335px; padding: 0 3px 0 12px;
    border-left: 1px solid #ececec; font-size: 13.3px; line-height: 18.6px; text-align: justify; hyphens: auto;
  }
  .aside-copy p + p { margin-top: 18px; }
  .site-footer {
    position: absolute; left: 58px; right: 76px; top: 742px; display: flex; justify-content: space-between;
    color: var(--white); font-size: 13.5px;
  }
  .site-footer a { color: var(--white); text-decoration: none; }
</style>
</head>
<body>
  <header class="utility-bar">
    <a class="utility-link is-account" href="#">
      <svg viewBox="0 0 20 20"><circle cx="10" cy="10" r="9.5" fill="#fff"/><path d="M6 10h6M9.5 7l3 3-3 3" stroke="#4f9a45" stroke-width="1.8" fill="none"/><rect x="12.5" y="5.5" width="2" height="9" fill="#4f9a45"/></svg>
      SIGN IN / REGISTER
    </a>
    <a class="utility-link" href="#" style="left:227px">
      <svg viewBox="0 0 20 20"><circle cx="10" cy="10" r="9.5" fill="#fff"/><rect x="7.5" y="4.5" width="5" height="4" fill="none" stroke="#4f9a45" stroke-width="1.4"/><rect x="4" y="11.5" width="5" height="4" fill="none" stroke="#4f9a45" stroke-width="1.4"/><rect x="11" y="11.5" width="5" height="4" fill="none" stroke="#4f9a45" stroke-width="1.4"/><path d="M10 8.5v3" stroke="#4f9a45" stroke-width="1.4"/></svg>
      CONTACT &nbsp;US
    </a>
    <a class="utility-link" href="#" style="left:355px">
      <svg viewBox="0 0 20 20"><circle cx="10" cy="10" r="9.5" fill="#fff"/><rect x="5" y="6.5" width="10" height="7" fill="none" stroke="#4f9a45" stroke-width="1.4"/><path d="M5 6.5l5 4 5-4" stroke="#4f9a45" stroke-width="1.4" fill="none"/></svg>
      SITEMAP
    </a>
  </header>

  <div class="brand">
    <div class="brand-name">Vorlaxen</div>
    <div class="brand-tagline">Accelerating revenue</div>
  </div>

  <nav class="main-nav">
    <a href="#">Home</a>
    <a href="#" class="is-active">Solutions</a>
    <a href="#">Delivery Model</a><span class="sep">|</span>
    <a href="#">Customers</a><span class="sep">|</span>
    <a href="#">Company</a><span class="sep">|</span>
    <a href="#">Careers</a>
  </nav>

  <div class="page-panel"></div>

  <aside class="side-menu">
    <div class="side-menu-title">
      <span class="marker"><svg width="8" height="8" viewBox="0 0 8 8"><path d="M1 0l6 4-6 4z" fill="#fff"/></svg></span>
      Managed Services
    </div>
    <ul>
      <li>Sales applications helpdesk</li>
      <li>Data Cleansing</li>
      <li>Service contract renewal</li>
      <li>Web content management</li>
    </ul>
  </aside>

  <section class="hero-banner" role="img" aria-label="Photo of two business people shaking hands in front of a stock chart">
    <div class="hero-banner-copy">
      <h2>Do more with less.</h2>
      <p>No upfront software, hardware,<br>people or training costs for you. Pay as you go.</p>
    </div>
  </section>

  <section class="feature-card">
    <div class="feature-card-image" role="img" aria-label="Photo of a meeting table with sales reports and pens"></div>
    <div class="feature-card-caption">Sales Operations Support</div>
  </section>

  <main class="content" lang="en">
    <h1><span class="kicker">Our Solutions:</span><span class="title">Managed Services</span></h1>
    <p>Lorem ipsum dolor sit amet, consectetur adipiscing elit. Proin augue felis, egestas quis imperdiet id, cursus sit amet est. Vestibulum consequat consectetur nisl non sodales. Donec viverra rhoncus turpis interdum aliquam. Ut imperdiet, risus varius aliquam lobortis, tortor quam hendrerit magna, imperdiet malesuada justo justo posuere mi. Praesent pretium consectetur tellus eu tempor. Duis iaculis sollicitudin mauris, eu posuere ligula dictum quis. Sed at lacus et dui condimentum ultrices. Aliquam cursus porta placerat. Suspendisse ut ante quam, lobortis laoreet ante. Aliquam ligula eros, bibendum rhoncus tristique sit amet, viverra a nunc. Cras aliquet, lectus eu facilisis tempor, lectus lacus vehicula felis, a tincidunt enim felis sit amet tellus.</p>
    <p>Fusce egestas, massa et placerat varius, urna odio elementum neque, aliquet mattis elit ipsum in ante. Maecenas mollis dolor id est vehicula et auctor turpis dignissim. Suspendisse lobortis eleifend lacus sit amet eleifend. Aenean a orci id mi scelerisque porttitor. Vestibulum lectus arcu, iaculis non iaculis ultrices, ultricies sit amet nisi. Nullam dictum nunc et metus dapibus scelerisque. Etiam quis sapien in purus consequat ornare. Praesent vitae ipsum lorem. Nullam ac orci mi, sed pellentesque dolor.</p>
  </main>

  <aside class="aside-copy" lang="en">
    <p>Vestibulum lectus arcu, iaculis non iaculis ultrices, ultricies sit amet nisi. Nullam dictum nunc et metus dapibus scelerisque. Etiam quis sapien in purus consequat ornare.</p>
    <p>Praesent vitae ipsum lorem. Nullam ac orci mi, sed pellen&shy;tesque dolor. Nullam dictum nunc et metus dapibus scelerisque. Etiam quis sapien in purus consequat ornare. Praesent vitae ipsum lorem. Nullam ac orci mi, sed pellen&shy;tesque dolor.</p>
  </aside>

  <footer class="site-footer">
    <div><a href="#">Contact Us</a> | <a href="#">Sitemap</a> &nbsp;| &nbsp;<a href="#">Disclaimer</a></div>
    <div>© 2010. Vorlaxen, Inc. All Rights Reserved</div>
  </footer>
</body>
</html>
```